Home page web design for a lawn specialist business

-The design must be based around the attached HPID (home page information design) called Turf Tidings HPID. I've attached Word and PDF versions - these are the same. The table boxes are just for approximate placement of information and you can use boxes and bold shapes for this design.

All fonts used in the HPID are only examples - you can use any Google font you wish.

- Text that is in orange is for your information only. Text to go on the design is black. Some instructions are in the HPID. Please be creative!

-The design needs to be modern and exciting - colours are to be the green of the logo, and white ...and then choose dark green, or dark grey or black.

Logo - attached (it's not great quality but don't worry, we'll replace it later)

- I've provided the images for the galleries - they are labelled and will match the name in the HPID. Please use the supplied images!

- Examples of some websites that have great design... don't copy them please but they are similar in look to what we are after....
www.qmbbuildworks.co.nz
http://www.rim-safeguard.co.nz/
http://www.lumenhomes.wb.gs/

Important: Width of content will be 1280 pixels when implemented as a web page but the winning design will need to supplied be on a 2000 pixel wide background so nav bars and background can extend outside the 1280 width.
Header height (without nav bar) 150-160 pixels.

We don't comment on individual designs but will choose a winning design promptly.

Industry/Entity Type

Business

Number of Pages Required

1 page

Font styles to use
Sans Serif

Requirements
Must have
• clean, modern, well-spaced design

```html
<!DOCTYPE html>
<html lang="en">
<head>
<meta charset="utf-8">
<title>Turf Tidings – Lawn Specialists</title>
<link rel="stylesheet" href="https://fonts.googleapis.com/css2?family=Oswald:wght@400;500;600&family=Roboto+Condensed:wght@400;700&display=swap">
<style>
:root{
  --lime:#9fe51c;
  --lime-soft:#b8f03a;
  --green:#6cb51a;
  --green-dark:#3f7f12;
  --ink:#111111;
  --charcoal:#2b2b2b;
  --grey-band:#efefef;
  --field:#e6e6e6;
  --white:#ffffff;
  --text:#333333;
}
*{box-sizing:border-box;margin:0;padding:0}
html,body{width:720px;height:1200px;overflow:hidden;background:var(--white)}
body{position:relative;font-family:"Roboto Condensed",Arial,sans-serif;color:var(--text)}
.abs{position:absolute}
.photo{position:absolute}

/* header */
.brand{left:116px;top:12px;display:flex;align-items:center;gap:6px}
.brand-dot{width:14px;height:14px;border-radius:50%;background:var(--lime)}
.brand-name{font-family:"Oswald",sans-serif;font-weight:500;font-size:15px;color:var(--green)}
.header-info{right:114px;top:6px;text-align:right}
.header-title{font-family:"Oswald",sans-serif;font-weight:600;font-size:16px;line-height:18px;color:var(--ink)}
.header-tag{font-size:8px;line-height:10px;font-weight:700;color:var(--ink)}
.header-phone{font-family:"Oswald",sans-serif;font-size:11px;line-height:14px;color:var(--green);font-weight:500;margin-top:2px}

/* nav */
.nav{left:104px;top:60px;width:512px;height:30px;background:var(--ink);display:flex;align-items:center;justify-content:space-between;list-style:none;padding-right:6px}
.nav li{font-family:"Oswald",sans-serif;font-size:9px;color:var(--white);padding:0 6px;height:30px;line-height:30px;white-space:nowrap}
.nav li.is-active{background:var(--lime);padding:0 10px}

/* hero */
.hero-before{left:104px;top:94px;width:252px;height:170px;background:linear-gradient(180deg,#cfd2cb 0%,#8a7f73 45%,#6f655a 100%)}
.hero-after{left:364px;top:94px;width:252px;height:170px;background:linear-gradient(180deg,#d7dbd2 0%,#5aa823 40%,#3f8e18 100%)}
.hero-label{left:0;width:100%;text-align:center;bottom:6px;font-family:"Oswald",sans-serif;font-weight:600;font-size:15px;color:var(--white);letter-spacing:.5px}

/* intro */
.intro{left:136px;top:280px;width:448px;text-align:center}
.intro-title{font-size:17px;line-height:20px;color:var(--green);font-weight:400}
.intro-sub{font-size:12px;line-height:15px;color:var(--ink)}
.intro-copy{font-size:9.5px;line-height:13px;color:var(--ink);margin-top:10px}

/* services */
.services{left:104px;top:414px;width:512px;height:389px;background:var(--grey-band)}
.card{position:absolute;width:194px;height:168px;background:var(--white);box-shadow:0 1px 3px rgba(0,0,0,.18);text-align:center}
.card .photo{left:0;top:0;width:194px;height:89px}
.card-title{position:absolute;top:95px;left:0;width:100%;font-weight:700;font-size:10px;color:var(--green)}
.card-copy{position:absolute;top:110px;left:14px;right:14px;font-size:6px;line-height:1.35;color:var(--text)}
.btn{display:inline-block;background:var(--ink);color:var(--white);font-size:5.5px;text-transform:uppercase;padding:4px 10px;border-radius:3px;white-space:nowrap}
.card .btn{position:absolute;left:50%;transform:translateX(-50%);top:141px}

/* promo */
.promo{left:104px;top:803px;width:512px;height:162px;background:var(--lime)}
.promo-video-title{left:40px;top:9px;width:190px;text-align:center;font-family:"Oswald",sans-serif;font-weight:500;font-size:8.5px;line-height:11px;color:var(--ink);white-space:nowrap}
.promo-video{left:53px;top:40px;width:168px;height:106px;background:linear-gradient(180deg,#b9c7b0 0%,#4e9a25 60%,#3a7d18 100%)}
.play{left:65px;top:34px}
.promo-text{left:267px;top:10px;width:232px;color:var(--white)}
.promo-heading{font-family:"Oswald",sans-serif;font-size:12px;font-weight:500}
.promo-copy{font-size:7px;line-height:1.35;margin-top:7px}
.promo .btn{position:absolute;left:342px;top:134px}

/* testimonial */
.quote{left:104px;top:965px;width:256px;height:101px;background:var(--charcoal);padding:22px 8px 0;text-align:center}
.quote-lead{font-size:7px;color:var(--lime-soft);white-space:nowrap}
.quote-body{font-size:6px;color:#dcdcdc;margin-top:6px;line-height:1.35}
.quote-cite{font-size:5px;color:#cfcfcf;text-align:right;margin-top:8px;line-height:1.25;padding-right:14px}
.mower-photo{left:360px;top:965px;width:256px;height:101px;background:linear-gradient(180deg,#7fbf3a 0%,#5fa02a 50%,#7bb83a 100%)}

/* footer */
.foot-nav{left:120px;top:1084px;list-style:none}
.foot-nav li{font-family:"Oswald",sans-serif;font-size:7px;color:var(--ink);line-height:9.4px;font-weight:500}
.foot-brand{left:186px;top:1120px;display:flex;align-items:center;gap:5px}
.quote-form{left:337px;top:1078px;width:270px;height:90px}
.form-title{font-family:"Oswald",sans-serif;font-weight:500;font-size:8.5px;line-height:1.15;color:var(--ink)}
.field{position:absolute;width:96px;height:15px;background:var(--field);border-radius:3px;font-size:6px;color:#888;text-align:center;line-height:15px}
.quote-form .btn{position:absolute;left:198px;top:70px;width:68px;text-align:center}
.grass-strip{left:104px;top:1170px;width:512px;height:30px;background:linear-gradient(180deg,#9ccf4a 0%,#4e9a1e 100%)}
</style>
</head>
<body>

<header>
  <div class="abs brand"><span class="brand-dot"></span><span class="brand-name">Turf Tidings</span></div>
  <div class="abs header-info">
    <div class="header-title">LAWN SPECIALISTS</div>
    <div class="header-tag">...from ground preparation to lawn aftercare</div>
    <div class="header-tag">Servicing the Auckland region</div>
    <div class="header-phone">0800 24 68 10</div>
  </div>
</header>

<ul class="abs nav">
  <li class="is-active">Home</li><li>About us</li><li>Services</li><li>Lawn care</li><li>Seasonal care</li><li>Hydroseeding</li><li>FAQs</li><li>Before &amp; After Gallery</li><li>Quote / Contact</li>
</ul>

<section>
  <div class="photo hero-before" role="img" aria-label="Bare prepared soil beside a white house before seeding">
    <span class="abs hero-label">BEFORE</span>
  </div>
  <div class="photo hero-after" role="img" aria-label="The same garden with a lush green lawn after seeding">
    <span class="abs hero-label">AFTER</span>
  </div>
</section>

<section class="abs intro">
  <h1 class="intro-title">You can always spot a Turf Tidings lawn</h1>
  <p class="intro-sub">It's the one that turns your neighbours green with envy.</p>
  <p class="intro-copy">If you want a lawn or playing field that looks good throughout the year, talk to us. Turf Tidings are New Zealand's experts in high quality grass seeding and lawn maintenance, creating the lushest lawns you'll ever see. With high-tech equipment, years of experience and expert aftercare, nobody knows grass like Turf Tidings. There are many factors that influence the quality of a lawn, including seasonality, growing conditions, shade, seed types, and time. A one-size-fits-all solution couldn't possibly guarantee a great lawn, so we provide personalised advice, a full range of seeding techniques</p>
</section>

<section class="abs services">
  <article class="card" style="left:53px;top:16px">
    <div class="photo" role="img" aria-label="Freshly hydroseeded garden lawn" style="background:linear-gradient(180deg,#6f8f4a,#2f8f7a)"></div>
    <h2 class="card-title">Grass seeding services</h2>
    <p class="card-copy">With a wide range of grass seed applications to choose from, including hydroseeding and instant lawn, there is an option to suit your property and your requirements.</p>
    <span class="btn">More about grass seeding</span>
  </article>
  <article class="card" style="left:266px;top:16px">
    <div class="photo" role="img" aria-label="Sprinkler watering green grass" style="background:linear-gradient(180deg,#8fcf4a,#3f8f1a)"></div>
    <h2 class="card-title">Lawn care maintenance</h2>
    <p class="card-copy">As well as lawn care services, the team at Turf Tidings provides helpful information for regular upkeep of your residential or commercial lawn.</p>
    <span class="btn">More about ongoing lawn care</span>
  </article>
  <article class="card" style="left:53px;top:204px">
    <div class="photo" role="img" aria-label="Green lawn in a fenced backyard" style="background:linear-gradient(180deg,#c9cbc3,#4fa82a)"></div>
    <h2 class="card-title">FAQs about grass seeding and lawn care</h2>
    <p class="card-copy">For more information, read our frequently asked questions regarding grass seeding and lawn care.</p>
    <span class="btn">Grass seeding &amp; lawn care FAQs</span>
  </article>
  <article class="card" style="left:266px;top:204px">
    <div class="photo" role="img" aria-label="Side by side before and after lawn photos" style="background:linear-gradient(90deg,#3f8f7a 0%,#3f8f7a 50%,#5aaa28 50%,#5aaa28 100%)"></div>
    <h2 class="card-title">Before and after lawn photos</h2>
    <p class="card-copy">See what you potential new lawn could look like by viewing a range of before and after lawn seeding photos.</p>
    <span class="btn">Before and after photos</span>
  </article>
</section>

<section class="abs promo">
  <h2 class="abs promo-video-title">Watch the video on how Turf Tidings can transform<br>your empty spaces into beautiful green grass lawns</h2>
  <div class="abs promo-video" role="img" aria-label="Video still of a house with a new green lawn">
    <svg class="abs play" width="38" height="38" viewBox="0 0 38 38" aria-hidden="true"><circle cx="19" cy="19" r="16" fill="none" stroke="#fff" stroke-width="3"/><path d="M15 11 L28 19 L15 27 Z" fill="#fff"/></svg>
  </div>
  <div class="abs promo-text">
    <h2 class="promo-heading">Turf Tidings...</h2>
    <p class="promo-copy">For all things grass, you need the best! Turf Tidings are skilled specialists when it comes to creating the perfect lawn for your property.</p>
    <p class="promo-copy">From pre-seeding preparation to a full range of grass seeding services and lawn after care options, you'll enjoy a healthy green lawn for many years.</p>
    <p class="promo-copy">Selling your property? Turf Tidings will add the wow factor to the outdoor areas of your home with a lush green lawn.</p>
  </div>
  <span class="btn">Find out more</span>
</section>

<section>
  <blockquote class="abs quote">
    <p class="quote-lead">"I would recommend Turf Tidings to anyone who wants an amazing lawn"</p>
    <p class="quote-body">"Testimonial here about how great Turf Tidings were to deal with and how they are so happy with the lawn and the after care services etc etc."</p>
    <p class="quote-cite">Dan Harlow<br>Homeowner, Albany</p>
  </blockquote>
  <div class="photo mower-photo" role="img" aria-label="Lawn mower cutting bright green grass"></div>
</section>

<footer>
  <ul class="abs foot-nav">
    <li>Home</li><li>About us</li><li>Services</li><li>Lawn care</li><li>Seasonal care</li><li>Hydroseeding</li><li>FAQs</li><li>Before &amp; After</li>
  </ul>
  <div class="abs foot-brand"><span class="brand-dot"></span><span class="brand-name">Turf Tidings</span></div>
  <div class="abs quote-form">
    <p class="form-title">Get a quote for your new lawn!<br>Fill in the form or phone us on 0800 24 68 10</p>
    <span class="field" style="left:17px;top:26px">First name</span>
    <span class="field" style="left:126px;top:26px">Last name</span>
    <span class="field" style="left:17px;top:46px">Email address</span>
    <span class="field" style="left:126px;top:46px">Contact phone</span>
    <span class="field" style="left:17px;top:66px">Details</span>
    <span class="btn">Call me back</span>
  </div>
  <div class="photo grass-strip" role="img" aria-label="Close-up of grass blades along the page bottom"></div>
</footer>

</body>
</html>
```